New Website Design for NAPTO.org

We are looking for a new website design for NAPTO.org. NAPTO is a non profit home inspector association based in California. Home Inspectors are people that come out and look at a house before it's purchased to let the buyer know of any defects that may exist.
Our site is based on Joomla so if you'll be able to make a Joomla 3 template as well, please let us know (not required, but a bonus).
We would like to see designs that incorporate royal blue, white and chrome into the site as that's our main business colors.
We would like a place for rotating banners though they don't need to be the same size as the current site.
We would like navigation to be easier to manage with menus only across the top (via drop down menus) where we are going to sort out the items currently on the side. Possibly the front page could have a graphic link to separate portals for Realtors, Home Buyers and Inspectors, but that's just one option.
We would like a good mobile design or something that will scale easily to mobile.
The Find an Inspector feature is important and should stand out. The ASK NAPTOr site
Current home page feels a bit busy. Would like to simplify a bit.
Non Profit

```html
<!DOCTYPE html>
<html lang="en">
<head>
<meta charset="utf-8">
<title>NAPTO – Home</title>
<link href="https://fonts.googleapis.com/css2?family=Noto+Sans:ital,wght@0,400;0,700;1,400;1,700&display=swap" rel="stylesheet">
<style>
:root{
  --page-bg:#1d1d1f;
  --white:#ffffff;
  --royal:#27428a;
  --royal-dark:#1f3576;
  --royal-light:#3a66a8;
  --nav-top:#2f4f9a;
  --nav-bottom:#223f87;
  --chrome-light:#f4f4f4;
  --chrome-dark:#c9c9cb;
  --field:#f2f2f2;
  --text-grey:#555;
  --field-text:#999;
}
*{margin:0;padding:0;box-sizing:border-box}
html,body{width:1200px;height:1031px;overflow:hidden}
body{background:var(--page-bg);font-family:"Noto Sans",sans-serif;color:var(--white);position:relative}
.page{position:absolute;left:120px;top:28px;width:960px}
.header{position:relative;height:127px;background:var(--white)}
.brand{position:absolute;left:19px;top:20px;display:flex;align-items:center;gap:10px}
.brand-mark{width:46px;height:46px;border-radius:50%;background:var(--royal)}
.brand-name{font-size:24px;font-weight:700;color:var(--royal);letter-spacing:1px}
.search{position:absolute;left:292px;top:0;width:668px;height:64px;
  background:linear-gradient(to bottom,var(--chrome-light),var(--chrome-dark));
  border-bottom-left-radius:22px;display:flex;align-items:center;color:var(--text-grey);font-size:14px}
.search-label{position:absolute;top:20px}
.search-label.distance{left:21px}
.search-label.from{left:246px}
.search-select{position:absolute;left:90px;top:21px;width:137px;height:28px;background:var(--field);
  color:var(--field-text);padding:4px 10px;font-size:14px}
.search-select svg{position:absolute;right:6px;top:11px}
.search-input{position:absolute;left:291px;top:21px;width:155px;height:28px;background:var(--white);
  color:var(--field-text);padding:4px 10px;font-size:14px}
.search-button{position:absolute;left:465px;top:20px;width:183px;height:27px;background:var(--royal);
  border:1px solid #1a2f6a;color:var(--white);font-size:13.5px;text-align:center;line-height:25px}
.login{position:absolute;right:20px;top:87px;display:flex;align-items:center;gap:9px;color:var(--royal);font-size:14.5px}
.nav{height:47px;background:linear-gradient(to bottom,var(--nav-top),var(--nav-bottom));display:flex;padding-left:12px}
.nav-item{font-size:12.2px;line-height:47px;padding:0 16px;border-right:1px solid #4c67a6;white-space:nowrap}
.nav-item:last-child{border-right:none}
.hero{position:relative;height:282px;background:linear-gradient(100deg,#5f7a3a 0%,#b9a48a 22%,#cdb7a0 45%,#8f959f 65%,#6c84b3 78%,#d6c2a6 100%)}
.hero-caption{position:absolute;left:244px;top:141px;width:461px;height:103px;color:var(--white);font-style:italic}
.hero-caption svg{position:absolute;left:0;top:0}
.hero-line1{position:absolute;left:54px;top:18px;font-size:22.5px;letter-spacing:.5px}
.hero-line2{position:absolute;left:54px;top:52px;font-size:28.5px;letter-spacing:.5px}
.portals{position:relative;height:218px;background:var(--white)}
.portal{position:absolute;top:27px;width:290px;height:159px;border-radius:6px;overflow:hidden;
  background:linear-gradient(to bottom,#ffffff,#d8d9dc);box-shadow:0 1px 4px rgba(0,0,0,.25)}
.portal-photo{position:absolute;right:0;top:0;width:190px;height:159px}
.portal-label{position:absolute;left:0;top:103px;height:38px;background:var(--royal-dark);
  font-weight:700;font-style:italic;font-size:24px;line-height:38px;padding-left:20px;
  clip-path:polygon(0 0,100% 0,calc(100% - 22px) 100%,0 100%)}
.footer{height:264px;background:linear-gradient(to bottom,var(--royal),var(--royal-light));position:relative;font-size:12.7px}
.col{position:absolute;top:27px}
.col h2{font-size:16px;font-weight:700;letter-spacing:.3px;margin-bottom:9px}
.col.who{left:19px;width:275px}
.col.who p{line-height:21.6px}
.col.news{left:336px;width:290px}
.col.contact{left:650px;width:300px}
.news-item{position:relative;padding-left:22px;margin-bottom:11px}
.news-item svg{position:absolute;left:0;top:2px}
.news-head{line-height:19px;margin-bottom:6px}
.news-head u{text-underline-offset:2px}
.news-item p{line-height:17px}
.col.contact p{line-height:21.6px;margin-bottom:9px}
.copyright{position:absolute;left:120px;top:980px;font-size:12.6px}
</style>
</head>
<body>
<div class="page">
  <header class="header">
    <div class="brand"><span class="brand-mark"></span><span class="brand-name">NAPTO</span></div>
    <form class="search">
      <span class="search-label distance">distance</span>
      <div class="search-select">20<svg width="10" height="7"><path d="M0 0h10L5 7z" fill="#888"/></svg></div>
      <span class="search-label from">from</span>
      <div class="search-input">Enter a city or ZIP</div>
      <div class="search-button">SEARCH FOR INSPECTOR</div>
    </form>
    <div class="login">
      <svg width="18" height="20" viewBox="0 0 18 20"><circle cx="9" cy="5" r="4.5" fill="#27428a"/><path d="M1 20c0-6 3.5-9 8-9s8 3 8 9z" fill="#27428a"/></svg>
      LOGIN
    </div>
  </header>
  <nav class="nav">
    <span class="nav-item" style="width:78px">HOME</span>
    <span class="nav-item" style="width:163px">FIND AN INSPECTOR</span>
    <span class="nav-item" style="width:196px">HOME BUYERS &amp; SELLERS</span>
    <span class="nav-item" style="width:169px">REAL ESTATE AGENTS</span>
    <span class="nav-item" style="width:115px">INSPECTORS</span>
    <span class="nav-item" style="width:103px">ASK NAPTO</span>
    <span class="nav-item">CONFERENCES</span>
  </nav>
  <section class="hero" role="img" aria-label="Two-storey house with palm tree and a smiling inspector holding a clipboard">
    <div class="hero-caption">
      <svg width="461" height="103"><polygon points="24,0 461,0 461,103 0,103" fill="rgba(40,40,45,.6)"/></svg>
      <div class="hero-line1">REAL ANSWER FROM</div>
      <div class="hero-line2">SEASONED INSPECTORS</div>
    </div>
  </section>
  <section class="portals">
    <div class="portal" style="left:19px">
      <div class="portal-photo" role="img" aria-label="Smiling realtor holding house keys" style="background:radial-gradient(ellipse at 55% 45%,#caa38e 0%,#6a4a3a 45%,rgba(30,30,30,.0) 75%)"></div>
      <div class="portal-label" style="width:185px">REALTOR</div>
    </div>
    <div class="portal" style="left:334px">
      <div class="portal-photo" role="img" aria-label="Happy home buyer holding banknotes" style="background:radial-gradient(ellipse at 50% 45%,#d9b98a 0%,#8a7a5a 45%,rgba(40,40,40,0) 75%)"></div>
      <div class="portal-label" style="width:221px">HOME BUYER</div>
    </div>
    <div class="portal" style="left:650px">
      <div class="portal-photo" role="img" aria-label="Inspector in blue hard hat with clipboard giving thumbs up" style="background:radial-gradient(ellipse at 50% 45%,#c9a28a 0%,#2b3a6e 45%,rgba(40,40,60,0) 75%)"></div>
      <div class="portal-label" style="width:204px">INSPECTOR</div>
    </div>
  </section>
  <footer class="footer">
    <div class="col who">
      <h2>WHO WE ARE</h2>
      <p>Established in 1976, NAPTO is a non-profit trade association, with chapters located throughout the state. NAPTO is a member-driven, hands-on organization that provides educational programming and on-going opportunities for its members to interact at both local and statewide NAPTO meetings and events.</p>
    </div>
    <div class="col news">
      <h2>LATEST NEWS</h2>
      <div class="news-item">
        <svg width="15" height="19" viewBox="0 0 15 19"><path d="M1 1h9l4 4v13H1z" fill="none" stroke="#fff" stroke-width="1.3"/><path d="M4 9h5M4 12h7M4 15h7" stroke="#fff" stroke-width="1.1"/></svg>
        <div class="news-head"><u>Schedule</u> 21.01.2013</div>
        <p>NAPTO Inspector Members have passed the proctored comprehensive California Home Inspector Exam</p>
      </div>
      <div class="news-item">
        <svg width="15" height="19" viewBox="0 0 15 19"><path d="M1 1h9l4 4v13H1z" fill="none" stroke="#fff" stroke-width="1.3"/><path d="M4 9h5M4 12h7M4 15h7" stroke="#fff" stroke-width="1.1"/></svg>
        <div class="news-head"><u>Schedule</u> 21.01.2013</div>
        <p>NAPTO Inspector Members have passed the proctored comprehensive California Home Inspector Exam</p>
      </div>
    </div>
    <div class="col contact">
      <h2>CONTACT US</h2>
      <p>2450 Alder Avenue Suite 310 Sacramento CA 95816-4402</p>
      <p>Hours: M-F, 8:00am - 5:00pm</p>
      <p>Phone: (800) 555-0142 or (916) 555-0187</p>
      <p>Fax: (916) 555-0163</p>
      <p>CEO@NAPTO.ORG or webmaster@NAPTO.ORG</p>
    </div>
  </footer>
</div>
<div class="copyright">Copyright © 2013 NAPTO - National Association of Property Technical Officers. All Rights Reserved.</div>
</body>
</html>
```